Craft Flavoured Beer Family Extension Desing

We are a Canadian craft brewery looking for the design of a new line of beer we wish to launch within an existing family of products. Our beers are high craft beers that retail for a significant price. Example, 4.49$ for 500 mL vs. 1.49$ for a 500 mL Valdmeer.

The line of beer that is being designed here is for a craft flavoured beer line targeted to women. This will be light tasting beers with light fruit flavors targeted to consumers who like beer but are not ready for the strong IPA which are generally found in the craft beer offerings.

The Mireille line, which is the name of this new product, is a ''cousin'' of the existing Gustave-Armand Line (more info below).

Target Market(s)

60% Females 40% Males - 21 to 40 years old

Industry/Entity Type

Brewery

Requirements
Must have
• The products will be an INDIRECT family/line extension of the Gustave-Armand line of products (design attached). There needs to be some similarities, but it cannot be too close. There are 3 main features on the Gustave-Armand label (attached) : (1) the font used for the Logo; (2) the shape of the label; (3) the motif printed on the label.
• The shape of the label must be different than the current shape.
• However, the font of the logo (Gustave-Armand) can be the same and the motif printed on the label can be used. Using one of these elements is sufficient to link this new brand with the Gustave-Armand brand.
• The name of the product will be MIREILLE
Nice to have
• The bottle, the size, the ABV will be different than for the Gustave-Armand beers.
• There will be 3 flavours initially : Blueberry, Grapefruit and Raspberry.
• There needs to be a back label, but if you design, you can use the exact same information as there is currently.
Should not have
• We don't want any fruit pictures or designs on the labels.

```html
<!DOCTYPE html>
<html lang="fr">
<head>
<meta charset="utf-8">
<title>Mireille – gamme aromatisée</title>
<link rel="stylesheet" href="https://fonts.googleapis.com/css2?family=Anton&family=Libre+Baskerville:wght@400;700&family=Pinyon+Script&family=Archivo+Black&display=swap">
<style>
  :root{
    --page:#ffffff;
    --ink:#111111;
    --label:#ffffff;
    --shadow:rgba(0,0,0,.32);
    --blue-ink:#62c6dc;
    --blue-band:#434b88;
    --blue-script:#62c6dc;
    --pink-ink:#f0b2d2;
    --pink-band:#6b1a4d;
    --pink-script:#f0b2d2;
    --yellow-ink:#f0e678;
    --yellow-band:#f0e672;
    --yellow-script:#f28734;
  }
  *{margin:0;padding:0;box-sizing:border-box}
  html,body{width:1200px;height:927px;overflow:hidden;background:var(--page)}
  .canvas{position:relative;width:1200px;height:927px}
  .label{
    position:absolute;top:212px;width:348px;height:464px;border-radius:50%;
    background:var(--label);box-shadow:7px 9px 9px var(--shadow);overflow:hidden;
  }
  .label--blueberry{left:48px;--accent:var(--blue-ink);--band:var(--blue-band);--script:var(--blue-script)}
  .label--raspberry{left:428px;--accent:var(--pink-ink);--band:var(--pink-band);--script:var(--pink-script)}
  .label--grapefruit{left:806px;--accent:var(--yellow-ink);--band:var(--yellow-band);--script:var(--yellow-script)}

  .crest{
    position:absolute;left:60px;top:18px;width:228px;height:130px;
    border-radius:50% 50% 18px 18px / 70% 70% 18px 18px;
    background:radial-gradient(ellipse at 50% 60%, color-mix(in srgb,var(--accent) 45%,#fff), color-mix(in srgb,var(--accent) 15%,#fff));
  }
  .brewery-arc{position:absolute;left:0;top:0;width:348px;height:200px}
  .brewery-arc text{font-family:"Libre Baskerville",serif;font-size:8.5px;letter-spacing:1px;fill:var(--ink)}
  .brewery-arc path.line{fill:none;stroke:var(--accent);stroke-width:1.2}

  .name{
    position:absolute;left:0;right:0;top:184px;text-align:center;
    font-family:"Anton",sans-serif;font-size:70px;line-height:1;letter-spacing:1px;
    color:var(--ink);
    text-shadow:-2px -2px 0 var(--label),-3px -3px 0 var(--ink),-4px -4px 0 var(--ink);
  }
  .band{position:absolute;left:8px;width:332px;top:264px;height:40px;background:var(--band)}
  .flavour{
    position:absolute;left:0;right:0;top:254px;text-align:center;
    font-family:"Pinyon Script",cursive;font-size:48px;line-height:1;color:var(--script);
  }
  .origin{
    position:absolute;left:0;right:0;top:318px;text-align:center;
    font-family:"Libre Baskerville",serif;font-size:12px;letter-spacing:3px;color:var(--ink);
  }
  .facts{position:absolute;left:0;top:336px;width:348px;height:30px}
  .facts__kind{
    position:absolute;left:51px;top:4px;font-family:"Archivo Black",sans-serif;
    font-size:11px;line-height:11px;letter-spacing:2px;color:var(--ink);
  }
  .facts__volume{
    position:absolute;left:138px;top:0;font-family:"Anton",sans-serif;font-size:25px;line-height:28px;color:var(--ink);
  }
  .facts__volume small{font-size:19px}
  .facts__abv{
    position:absolute;left:262px;top:2px;width:36px;text-align:center;
    font-family:"Anton",sans-serif;font-size:13px;line-height:12px;color:var(--ink);
  }
  .facts__abv span{display:block;font-family:"Libre Baskerville",serif;font-size:8px;letter-spacing:-.3px}
  .flourish{
    position:absolute;left:94px;top:384px;width:160px;height:44px;border-radius:40%;
    background:radial-gradient(ellipse at center, color-mix(in srgb,var(--accent) 55%,#fff), color-mix(in srgb,var(--accent) 12%,#fff));
  }
</style>
</head>
<body>
<main class="canvas">

  <article class="label label--blueberry">
    <div class="crest" role="img" aria-label="Ornamental scrollwork crest in light blue"></div>
    <svg class="brewery-arc" viewBox="0 0 348 200">
      <path class="line" d="M60 170 Q174 118 288 170"/>
      <path id="arc-b" d="M86 172 Q174 132 262 172" fill="none"/>
      <text><textPath href="#arc-b" startOffset="50%" text-anchor="middle">· BRASSERIE DEUX RIVES ·</textPath></text>
    </svg>
    <h1 class="name">MIREILLE</h1>
    <div class="band"></div>
    <p class="flavour">Blueberry</p>
    <p class="origin">BRASSÉE AU QUÉBEC</p>
    <div class="facts">
      <p class="facts__kind">BIÈRE<br>BEER</p>
      <p class="facts__volume">500 <small>mL</small></p>
      <p class="facts__abv">5%<span>alc./vol.</span></p>
    </div>
    <div class="flourish" role="img" aria-label="Small ornamental leaf flourish in light blue"></div>
  </article>

  <article class="label label--raspberry">
    <div class="crest" role="img" aria-label="Ornamental scrollwork crest in soft pink"></div>
    <svg class="brewery-arc" viewBox="0 0 348 200">
      <path class="line" d="M60 170 Q174 118 288 170"/>
      <path id="arc-r" d="M86 172 Q174 132 262 172" fill="none"/>
      <text><textPath href="#arc-r" startOffset="50%" text-anchor="middle">· BRASSERIE DEUX RIVES ·</textPath></text>
    </svg>
    <h1 class="name">MIREILLE</h1>
    <div class="band"></div>
    <p class="flavour">Raspberry</p>
    <p class="origin">BRASSÉE AU QUÉBEC</p>
    <div class="facts">
      <p class="facts__kind">BIÈRE<br>BEER</p>
      <p class="facts__volume">500 <small>mL</small></p>
      <p class="facts__abv">5%<span>alc./vol.</span></p>
    </div>
    <div class="flourish" role="img" aria-label="Small ornamental leaf flourish in soft pink"></div>
  </article>

  <article class="label label--grapefruit">
    <div class="crest" role="img" aria-label="Ornamental scrollwork crest in pale yellow"></div>
    <svg class="brewery-arc" viewBox="0 0 348 200">
      <path class="line" d="M60 170 Q174 118 288 170"/>
      <path id="arc-g" d="M86 172 Q174 132 262 172" fill="none"/>
      <text><textPath href="#arc-g" startOffset="50%" text-anchor="middle">· BRASSERIE DEUX RIVES ·</textPath></text>
    </svg>
    <h1 class="name">MIREILLE</h1>
    <div class="band"></div>
    <p class="flavour">Grapefruit</p>
    <p class="origin">BRASSÉE AU QUÉBEC</p>
    <div class="facts">
      <p class="facts__kind">BIÈRE<br>BEER</p>
      <p class="facts__volume">500 <small>mL</small></p>
      <p class="facts__abv">5%<span>alc./vol.</span></p>
    </div>
    <div class="flourish" role="img" aria-label="Small ornamental leaf flourish in pale yellow"></div>
  </article>

</main>
</body>
</html>
```